Poster for a 100 y.o. Tennis Tournament

I would like a poster designed to promote our tennis tournament but I'd like to avoid some of the clichés like the shadow of a player serving. Just well styled text would be fine but some clever imagery would be a bonus.
Highlighting the fact our tournament has been running for over 100 years would be nice so a retro design would work. But that doesn't mean a modern design, for example a minimalist approach utilising the lines of a tennis court, wouldn't work.
Updates

Our tennis committee is now in the process of short listing and will provide an update within 48 hours.

Industry/Entity Type

Court

Requirements
Must have
• The poster must contain the following text at a minimum:
"Marbury Tennis Tournament"/"Since 1908"
"9 March - 11 March, 2013" or "9-11 March, 2013", etc
"www.marburytennis.com.au"

The poster must be reproducible in colour and black & white, or at least have an alternate for black & white.

The poster must be usable in both A3 and A4 sizes.
Nice to have
• The poster should contain the following text:
"Championship"
"Handicap"
"Seniors"
"Juniors"
Each above may be optionally succeeded by "Singles & Doubles", e.g. "Championship Singles & Doubles". It would actually be clearer if this additional text was used but would be repetitive, so alternate text "Singles & Doubles in all categories" might also be used. Alternatives for variety (with the first word the focus): "Championship Singles & Doubles", "Handicap Singles & Doubles", "Seniors 35+ & 50+", "Juniors 18&U, 14&U"

Ideally the poster will provision room for four to eight sponsors logos, preferably at the bottom, but failure to do this is not a show stopper.

The following text may also be used:
"Entries close February 24"
"Tollard Plate Weekend"

Attached is a photo of one of the old trophies. Utilisation of the curved style of the "Marbury Tennis Tournament" text would fit in with the history if the tournament.

The ability to reuse elements of the poster in a single page website used to promote the tournament would be an advantage (as it will provide consistency).

If you could have an image of a tennis ball that conveys the same energy as the clock/tyre image in the attached "Under the Glass Moon" poster, that would be cool. Or using split imagery of a wooden racquet and a modern racquet, but with some energy, would also be good. These are just ideas though and by no means essential.

I've also attached a photo of a t-shirt with a poster layout I thought looked good.

Some additional text that can be used:
"Brand new courts"
"Brindle Park, Oakhurst Tce, Marbury"
"Phone 0427 318 642"
"Prizes and Trophies"

```html
<!DOCTYPE html>
<html lang="en">
<head>
<meta charset="utf-8">
<title>Marbury Tennis Tournament</title>
<link href="https://fonts.googleapis.com/css2?family=Alfa+Slab+One&family=Archivo+Black&display=swap" rel="stylesheet">
<style>
  :root {
    --backdrop: #e9e9e9;
    --kraft-light: #c2a583;
    --kraft-mid: #b2936f;
    --kraft-dark: #9c7c5a;
    --rust: #7a3410;
    --rust-deep: #5a2408;
    --ochre: #b16f1c;
    --ink: #2b2623;
    --cream: #fff8ea;
    --pale-gold: #fbe7b4;
    --sponsor-panel: #ffffff;
  }
  html, body {
    margin: 0;
    width: 901px;
    height: 1200px;
    overflow: hidden;
    background: var(--backdrop);
  }
  .poster {
    position: absolute;
    left: 86px;
    top: 92px;
    width: 716px;
    height: 1016px;
  }
  .poster svg { display: block; width: 100%; height: 100%; }
  .display { font-family: "Alfa Slab One", "Rockwell", serif; }
  .sans { font-family: "Archivo Black", "Arial Black", sans-serif; }
</style>
</head>
<body>
<div class="poster">
  <svg viewBox="86 92 716 1016" xmlns="http://www.w3.org/2000/svg">
    <defs>
      <radialGradient id="kraft" cx="45%" cy="35%" r="80%">
        <stop offset="0" stop-color="var(--kraft-light)"/>
        <stop offset="0.6" stop-color="var(--kraft-mid)"/>
        <stop offset="1" stop-color="var(--kraft-dark)"/>
      </radialGradient>
      <radialGradient id="artTone" cx="55%" cy="45%" r="60%">
        <stop offset="0" stop-color="#d9c7ad"/>
        <stop offset="0.5" stop-color="#8a6a4a"/>
        <stop offset="1" stop-color="#b69773" stop-opacity="0"/>
      </radialGradient>
      <path id="titleArc" d="M182,415 A280,280 0 0 1 730,380"/>
    </defs>

    <rect class="paper" x="86" y="92" width="716" height="1016" fill="url(#kraft)"/>

    <rect class="hero-art" x="200" y="240" width="420" height="370" rx="40" fill="url(#artTone)"
          role="img" aria-label="Grunge illustration of a tennis racquet, a black ball, old sneakers and a brushed court corner"/>

    <text class="display title" font-size="42" fill="var(--rust)" stroke="var(--cream)" stroke-width="2.5" paint-order="stroke">
      <textPath href="#titleArc" startOffset="0" textLength="745" lengthAdjust="spacing">Marbury Tennis Tournament</textPath>
    </text>

    <text class="sans tagline" font-size="17" fill="var(--ink)" transform="translate(120,602) rotate(-35)">Brand new courts</text>
    <text class="sans tagline" font-size="17" fill="var(--ink)" transform="translate(612,578) rotate(-90)">Prizes and Trophies</text>

    <g class="heritage">
      <text class="display" x="337" y="660" font-size="38" fill="var(--rust)">Since 1</text>
      <text class="sans" x="497" y="692" font-size="112" fill="var(--ink)">9</text>
      <text class="display" x="573" y="626" font-size="36" fill="var(--rust)">08</text>
      <text class="display" x="576" y="652" font-size="20" fill="var(--ink)">to 11 March, 2013</text>
    </g>

    <g class="events-band">
      <polygon points="86,790 600,705 600,855 86,942" fill="var(--rust)"/>
      <g transform="rotate(-5 340 830)" fill="var(--cream)">
        <text class="display" x="126" y="822" font-size="29">Singles</text>
        <text class="display" x="178" y="860" font-size="29">&amp;</text>
        <text class="display" x="118" y="898" font-size="29">Doubles</text>
        <text class="display" x="284" y="880" font-size="110" fill="var(--ochre)">{</text>
        <text class="display" x="326" y="760" font-size="20">Championship</text>
        <text class="display" x="326" y="786" font-size="20">Handicap</text>
        <text class="display" x="326" y="812" font-size="20">Seniors 35+ &amp; 50+</text>
        <text class="display" x="326" y="838" font-size="20">Juniors 18&amp;U, 14&amp;U</text>
      </g>
    </g>

    <g class="entries-box">
      <polygon points="578,722 802,678 802,692 592,734 592,868 580,870" fill="var(--ink)"/>
      <polygon points="590,720 802,678 802,815 592,865" fill="var(--ochre)"/>
      <g transform="rotate(-8 700 760)" fill="var(--cream)">
        <text class="display" x="604" y="752" font-size="22">Entries close</text>
        <text class="display" x="604" y="778" font-size="22">February 24</text>
        <text class="display" x="600" y="818" font-size="14" fill="var(--pale-gold)">Tollard Plate Weekend</text>
      </g>
    </g>

    <g class="venue" fill="var(--cream)">
      <text class="display" font-size="19" transform="translate(163,968) rotate(-9.4)">Brindle Park, Oakhurst Tce, Marbury | Phone 0427 318 642</text>
      <text class="display web" font-size="15" transform="translate(560,978) rotate(-9.4)">www.marburytennis.com.au</text>
    </g>

    <rect class="footer-rule" x="86" y="990" width="716" height="6" fill="var(--rust-deep)"/>
    <rect class="sponsor-panel" x="86" y="996" width="716" height="101" fill="var(--sponsor-panel)"/>
    <rect class="footer-rule" x="86" y="1097" width="716" height="11" fill="var(--rust-deep)"/>
  </svg>
</div>
</body>
</html>
```